Coffee label for coffee brand - Kettle Lane coffee

We want someone to design a label for packaging of a coffee line. The design will then be printed on stickers.

It is called Kettle Lane Coffee (logo enclosed) I want to incorporate a streetscape and the idea is that with every different coffee it will be a different colour (we have 6 varieties at the moment) with a black background. It needs to have a modern feel.

It needs to have a blank area towards the bottom for the type of coffee which we will print later on)

text to include

'Roasting exceptional coffee'

Target Market(s)

Coffee drinkers - modern feel

Font styles to use
Sans Serif

Colors
f78f20
9bcb3b
33a6d7
b768aa

Requirements
Must have
• the logo incorporated
• Space for coffee variety
• Quote' Roasting exceptional coffee'
Nice to have
• Streetscape theme incorporated - bright colour varieties (would love metallic) (on black background)

```html
<!DOCTYPE html>
<html lang="en">
<head>
<meta charset="utf-8">
<title>Kettle Lane Coffee – Label Range</title>
<link href="https://fonts.googleapis.com/css2?family=Montserrat:wght@500;600&family=Oswald:wght@500;600&display=swap" rel="stylesheet">
<style>
  :root {
    --ink: #0c0c0c;
    --paper: #ffffff;
    --text-dark: #151515;
    --bean-dark: #4a2616;
    --bean-mid: #7a4128;
    --bean-light: #a86c48;
    --cyan: #3ad4e6;
    --cyan-badge: #3291c2;
    --lime: #c8ec3f;
    --lime-badge: #6db33f;
    --magenta: #d86ce0;
    --magenta-badge: #8d5194;
    --amber-top: #f59a1e;
    --amber-bottom: #f7cc22;
    --amber-badge: #e47a1f;
    --silver: #e9e9e9;
    --silver-badge: #dadada;
  }
  * { box-sizing: border-box; margin: 0; padding: 0; }
  html, body { width: 1200px; height: 1200px; overflow: hidden; background: var(--paper); }
  .range { position: relative; width: 1200px; height: 1200px; }

  .label {
    position: absolute;
    width: 34.4em; height: 50.5em;
    font-size: 10px;
    background: var(--band);
    overflow: hidden;
  }
  .label--feature { font-size: 11.86px; }

  .label__top {
    position: absolute; left: 0; top: 0; width: 100%; height: 24.8em;
    background: var(--ink);
  }
  .wordmark {
    position: absolute; left: 0; right: 0; top: 9.6em;
    text-align: center; color: var(--paper);
    font-family: "Oswald", sans-serif; font-weight: 600;
    text-transform: uppercase; line-height: 1.05;
  }
  .wordmark__name { display: block; font-size: 4.4em; letter-spacing: 0.02em; }
  .wordmark__sub { display: block; font-size: 2.2em; letter-spacing: 0.3em; margin-top: 0.15em; }

  .label__weights {
    position: absolute; top: 27.6em; left: 0; width: 100%;
    font-family: "Montserrat", sans-serif; font-weight: 600;
    color: var(--text-dark);
  }
  .weight { position: absolute; font-size: 1.5em; line-height: 1; }
  .weight--imperial { left: 2.6em; }
  .weight--metric { right: 2.4em; }

  .beans {
    position: absolute; left: 0; width: 100%; top: 33em; height: 10.6em;
    background: radial-gradient(ellipse at 50% 50%, var(--bean-light) 0%, var(--bean-mid) 45%, var(--bean-dark) 100%);
  }

  .badge {
    position: absolute; left: 50%; top: 29.2em;
    width: 13.2em; height: 13.2em; margin: -6.6em 0 0 -6.6em;
    border-radius: 50%; background: var(--badge);
    display: flex; align-items: center; justify-content: center;
  }
  .badge__quote {
    text-align: center;
    font-family: "Montserrat", sans-serif; font-weight: 500;
    font-size: 1.3em; line-height: 1.3; color: var(--text-dark);
    text-transform: uppercase;
  }

  .label__info {
    position: absolute; left: 0; right: 0; top: 44.8em;
    text-align: center; color: var(--text-dark);
    font-family: "Oswald", sans-serif; font-weight: 500;
    text-transform: uppercase; line-height: 1;
  }
  .label__info span { font-size: 2.3em; }

  .label--cyan { left: 42px; top: 52px; --band: var(--cyan); --badge: var(--cyan-badge); }
  .label--lime { left: 832px; top: 52px; --band: var(--lime); --badge: var(--lime-badge); }
  .label--magenta { left: 53px; top: 652px; --band: var(--magenta); --badge: var(--magenta-badge); }
  .label--amber { left: 830px; top: 652px; --band: linear-gradient(var(--amber-top), var(--amber-bottom)); --badge: var(--amber-badge); }
  .label--silver { left: 408px; top: 320px; --band: var(--silver); --badge: var(--silver-badge); }
</style>
</head>
<body>
<main class="range">

  <section class="label label--cyan">
    <div class="label__top"><div class="wordmark"><span class="wordmark__name">Kettle Lane</span><span class="wordmark__sub">Coffee</span></div></div>
    <div class="label__weights"><span class="weight weight--imperial">12.OZ</span><span class="weight weight--metric">340 G</span></div>
    <div class="beans" role="img" aria-label="Band of roasted coffee beans"></div>
    <div class="badge"><p class="badge__quote">Roasting<br>Exceptional<br>Coffee</p></div>
    <p class="label__info"><span>Products Info</span></p>
  </section>

  <section class="label label--lime">
    <div class="label__top"><div class="wordmark"><span class="wordmark__name">Kettle Lane</span><span class="wordmark__sub">Coffee</span></div></div>
    <div class="label__weights"><span class="weight weight--imperial">12.OZ</span><span class="weight weight--metric">340 G</span></div>
    <div class="beans" role="img" aria-label="Band of roasted coffee beans"></div>
    <div class="badge"><p class="badge__quote">Roasting<br>Exceptional<br>Coffee</p></div>
    <p class="label__info"><span>Products Info</span></p>
  </section>

  <section class="label label--magenta">
    <div class="label__top"><div class="wordmark"><span class="wordmark__name">Kettle Lane</span><span class="wordmark__sub">Coffee</span></div></div>
    <div class="label__weights"><span class="weight weight--imperial">12.OZ</span><span class="weight weight--metric">340 G</span></div>
    <div class="beans" role="img" aria-label="Band of roasted coffee beans"></div>
    <div class="badge"><p class="badge__quote">Roasting<br>Exceptional<br>Coffee</p></div>
    <p class="label__info"><span>Products Info</span></p>
  </section>

  <section class="label label--amber">
    <div class="label__top"><div class="wordmark"><span class="wordmark__name">Kettle Lane</span><span class="wordmark__sub">Coffee</span></div></div>
    <div class="label__weights"><span class="weight weight--imperial">12.OZ</span><span class="weight weight--metric">340 G</span></div>
    <div class="beans" role="img" aria-label="Band of roasted coffee beans"></div>
    <div class="badge"><p class="badge__quote">Roasting<br>Exceptional<br>Coffee</p></div>
    <p class="label__info"><span>Products Info</span></p>
  </section>

  <section class="label label--silver label--feature">
    <div class="label__top"><div class="wordmark"><span class="wordmark__name">Kettle Lane</span><span class="wordmark__sub">Coffee</span></div></div>
    <div class="label__weights"><span class="weight weight--imperial">12.OZ</span><span class="weight weight--metric">340 G</span></div>
    <div class="beans" role="img" aria-label="Band of roasted coffee beans"></div>
    <div class="badge"><p class="badge__quote">Roasting<br>Exceptional<br>Coffee</p></div>
    <p class="label__info"><span>Products Info</span></p>
  </section>

</main>
</body>
</html>
```